Vostra new design for business cards we want to change our existing design. Logo must remain the same

Hello we are the company VoSTra and offer various services regarding transportation and disposal. In addition to our main acquisition of van rental, we also offer disposal and express transportation, so we need new business card designs for our business. Our elders have their time and do not like it anymore. We want to change our existing design. Logo must remain the same as well as the color blue, whether dark or light Does not play a big role in the best medium blue. Logo must be present on the front side. As well as telephone, email, web and location. Big enough but not too big. Back can be redesigned Logo as well as name VoSTra must be present. Important is the text: Van rental Disposal and clearing express transportation. Without bail in red should be noted somewhere. it should be modern but not too playful. rather serious but no beating company Thank you very much

Target Market(s)

Private customers as well as companies we want to change our existing design. Logo must remain the same as well as the color blue, whether dark or light Does not play a big role in the best medium blue. Logo must be present on the front side. As well as telephone, email, web and location. Big enough but not too big. Back can be redesigned Logo as well as name VoSTra must be present. Important is the text: Van rental Disposal and clearing express transportation. Without bail in red should be noted somewhere. it should be modern but not too playful. rather serious but no beating company Thank you very much

Industry/Entity Type

Car Rental

Contact Information for Business Card

we want to change our existing design. Logo must remain the same as well as the color blue, whether dark or light Does not play a big role in the best medium blue.
Logo must be present on the front side.
As well as telephone, email, web and location. Big enough but not too big.
Back can be redesigned Logo as well as name VoSTra must be present.
Important is the text:
Van rental
Disposal and clearing
Express transportation.
Without bail in red should be noted somewhere.
it should be modern but not too playful. rather serious but no beating company
Thank you very much

Font styles to use
Sans Serif

Colors
33a6d7
ec1f27
0692cd
3277b5

Requirements
Must have
• logo and name VoSTra as described in the above text must have it. we want to change our existing design. Logo must remain the same as well as the color blue, whether dark or light Does not play a big role in the best medium blue. Logo must be present on the front side. As well as telephone, email, web and location. Big enough but not too big. Back can be redesigned Logo as well as name VoSTra must be present. Important is the text: Van rental Disposal and clearing express transportation. Without bail in red should be noted somewhere. it should be modern but not too playful. rather serious but no beating company Thank you very much
Nice to have
• see description we want to change our existing design. Logo must remain the same as well as the color blue, whether dark or light Does not play a big role in the best medium blue. Logo must be present on the front side. As well as telephone, email, web and location. Big enough but not too big. Back can be redesigned Logo as well as name VoSTra must be present. Important is the text: Van rental Disposal and clearing express transportation. Without bail in red should be noted somewhere. it should be modern but not too playful. rather serious but no beating company Thank you very much
Should not have
• Blue White and little red we want to change our existing design. Logo must remain the same as well as the color blue, whether dark or light Does not play a big role in the best medium blue. Logo must be present on the front side. As well as telephone, email, web and location. Big enough but not too big. Back can be redesigned Logo as well as name VoSTra must be present. Important is the text: Van rental Disposal and clearing express transportation. Without bail in red should be noted somewhere. it should be modern but not too playful. rather serious but no beating company Thank you very much

```html
<!DOCTYPE html>
<html lang="en">
<head>
<meta charset="utf-8">
<title>Vostra Business Card</title>
<link rel="stylesheet" href="https://fonts.googleapis.com/css2?family=Roboto:wght@400;500;700&family=Roboto+Condensed:wght@400;700&display=swap">
<style>
  :root {
    --stage: #e9e7e4;
    --card-front: #f4f4f4;
    --card-back: #1b1c1e;
    --brand-blue: #3277b5;
    --steel: #7f97b3;
    --ink: #4f4f4f;
    --rule: #cfcfcf;
    --white: #ffffff;
    --alert-red: #ec1f27;
  }
  * { margin: 0; padding: 0; box-sizing: border-box; }
  html, body {
    width: 1200px;
    height: 960px;
    overflow: hidden;
    background: var(--stage);
    font-family: "Roboto", Arial, sans-serif;
  }
  .canvas { position: relative; width: 1200px; height: 960px; }

  .card { position: absolute; width: 600px; height: 342px; box-shadow: 0 3px 8px rgba(0,0,0,.25); }

  /* Front */
  .card-front { left: 314px; top: 113px; background: var(--card-front); }
  .brand {
    position: absolute; left: 72px; top: 130px;
    display: flex; align-items: center; gap: 12px;
  }
  .brand-mark { width: 40px; height: 40px; background: var(--brand-blue); }
  .brand-name {
    font-family: "Roboto", Arial, sans-serif;
    font-weight: 700; font-size: 36px; letter-spacing: 1px;
    color: var(--brand-blue);
  }
  .divider {
    position: absolute; left: 348px; top: 87px;
    width: 1px; height: 156px; background: var(--rule);
  }
  .contact { position: absolute; left: 381px; top: 83px; color: var(--ink); }
  .contact-name {
    font-family: "Roboto Condensed", Arial, sans-serif;
    font-weight: 700; font-size: 21px; color: var(--brand-blue); line-height: 24px;
  }
  .contact-role {
    font-family: "Roboto Condensed", Arial, sans-serif;
    font-weight: 400; font-size: 16px; color: var(--steel);
    line-height: 18px; margin-top: 0; letter-spacing: .3px;
  }
  .contact-address { font-size: 14.5px; line-height: 19px; margin-top: 10px; }
  .contact-lines { list-style: none; margin-top: 9px; font-size: 14.5px; line-height: 19px; }
  .contact-lines li { display: flex; align-items: center; gap: 8px; }
  .contact-lines svg { width: 13px; height: 13px; fill: var(--brand-blue); flex: none; }
  .band { position: absolute; bottom: 0; height: 8px; }
  .band-blue { left: 0; width: 347px; background: var(--brand-blue); }
  .band-steel { left: 349px; right: 0; background: var(--steel); }

  /* Back */
  .card-back { left: 311px; top: 472px; background: var(--card-back); }
  .back-brand {
    position: absolute; left: 0; right: 0; top: 108px;
    text-align: center;
    font-family: "Roboto", Arial, sans-serif;
    font-weight: 700; font-size: 64px; letter-spacing: 3px;
    color: var(--brand-blue);
  }
  .services {
    position: absolute; left: 0; right: 0; top: 275px;
    text-align: center; color: var(--white);
    font-size: 15px; line-height: 22px;
  }
  .services-note { color: var(--alert-red); }
</style>
</head>
<body>
<main class="canvas">
  <section class="card card-front">
    <div class="brand">
      <span class="brand-mark"></span>
      <span class="brand-name">VOSTRA</span>
    </div>
    <div class="divider"></div>
    <div class="contact">
      <p class="contact-name">LUKAS BRANDT</p>
      <p class="contact-role">CEO/FOUNDER</p>
      <p class="contact-address">Lindenweg 14<br>8500 Frauenfeld</p>
      <ul class="contact-lines">
        <li>
          <svg viewBox="0 0 24 24" aria-hidden="true"><path d="M6.6 10.8a15.1 15.1 0 0 0 6.6 6.6l2.2-2.2c.3-.3.7-.4 1-.2 1.1.4 2.3.6 3.6.6.6 0 1 .4 1 1V20c0 .6-.4 1-1 1A17 17 0 0 1 3 4c0-.6.4-1 1-1h3.5c.6 0 1 .4 1 1 0 1.3.2 2.5.6 3.6.1.3 0 .7-.2 1z"/></svg>
          +41 76 402 18 37
        </li>
        <li>
          <svg viewBox="0 0 24 24" aria-hidden="true"><path d="M2 5h20v14H2zm2 2v1l8 5 8-5V7l-8 5z"/></svg>
          info@vostra.ch
        </li>
        <li>
          <svg viewBox="0 0 24 24" aria-hidden="true"><path d="M12 2a10 10 0 1 0 0 20 10 10 0 0 0 0-20zm-1 17.9A8 8 0 0 1 4.2 10.2L9 15v1a2 2 0 0 0 2 2zm6.9-2.5A2 2 0 0 0 16 16h-1v-3a1 1 0 0 0-1-1H8v-2h2a1 1 0 0 0 1-1V7h2a2 2 0 0 0 2-2v-.4a8 8 0 0 1 2.9 12.8z"/></svg>
          www.VoSTra.ch
        </li>
      </ul>
    </div>
    <div class="band band-blue"></div>
    <div class="band band-steel"></div>
  </section>

  <section class="card card-back">
    <p class="back-brand">VOSTRA</p>
    <p class="services">Van rental &bull; Disposal &amp; clearing &bull; Express transportation<br><span class="services-note">Without bail</span></p>
  </section>
</main>
</body>
</html>
```